Letter head incorporating Our values and our Pebble & Fern logo

here are our current letterheads, similar look and feel but incorporating our values logo too.
I have attached some of our flyers to give an idea of our look and feel of our brand

```html
<!DOCTYPE html>
<html lang="en">
<head>
<meta charset="utf-8">
<title>Pebble &amp; Fern Letterhead</title>
<link href="https://fonts.googleapis.com/css2?family=Montserrat:wght@400;500&family=Open+Sans:wght@400;600&display=swap" rel="stylesheet">
<style>
  :root {
    --backdrop: #e4e4e6;
    --paper: #ffffff;
    --brand-blue: #29a8e0;
    --ink: #3a3a3c;
    --ink-soft: #555558;
    --wash-yellow: #fff7cf;
    --wash-blue: #e3f3fc;
  }
  html, body {
    margin: 0;
    width: 1200px;
    height: 960px;
    overflow: hidden;
    background: var(--backdrop);
  }
  .letterhead {
    position: absolute;
    left: 262px;
    top: 20px;
    width: 676px;
    height: 920px;
    background: var(--paper);
    box-shadow: 0 6px 22px rgba(0,0,0,0.12);
    font-family: "Open Sans", sans-serif;
    color: var(--ink);
  }
  .brand {
    position: absolute;
    left: 56px;
    top: 62px;
    display: flex;
    align-items: center;
    gap: 12px;
  }
  .brand-square {
    width: 40px;
    height: 40px;
    background: var(--brand-blue);
  }
  .brand-name {
    font-family: "Open Sans", sans-serif;
    font-weight: 600;
    font-size: 22px;
    color: var(--brand-blue);
  }
  .contact {
    position: absolute;
    left: 372px;
    top: 54px;
    padding-left: 18px;
    border-left: 1.5px solid var(--brand-blue);
    font-family: "Montserrat", sans-serif;
    font-style: normal;
    font-size: 11.5px;
    line-height: 1.55;
    color: var(--ink);
  }
  .contact-address { margin: 0 0 2px; }
  .contact-row { display: flex; align-items: center; gap: 7px; }
  .contact-row svg { width: 10px; height: 10px; fill: var(--brand-blue); flex: none; }
  .recipient {
    position: absolute;
    left: 56px;
    top: 220px;
    font-family: "Montserrat", sans-serif;
    font-size: 10.5px;
    line-height: 1.5;
    color: var(--ink-soft);
  }
  .recipient-name { font-size: 13px; color: var(--ink); letter-spacing: 0.3px; }
  .values-wash {
    position: absolute;
    left: 250px;
    top: 250px;
    width: 300px;
    height: 330px;
    border-radius: 40% 45% 40% 50%;
    background: radial-gradient(ellipse at 45% 40%, var(--wash-yellow) 0%, var(--wash-yellow) 45%, var(--wash-blue) 75%, rgba(255,255,255,0) 100%);
    opacity: 0.85;
  }
  .body {
    position: absolute;
    left: 110px;
    top: 300px;
    width: 500px;
    font-size: 10.5px;
    line-height: 1.65;
    color: var(--ink);
  }
  .body p { margin: 0 0 20px; }
  .signoff {
    position: absolute;
    left: 270px;
    top: 700px;
    font-size: 11px;
    color: var(--ink-soft);
  }
  .signoff-name {
    margin-top: 44px;
    font-family: "Montserrat", sans-serif;
    font-size: 13px;
    color: var(--ink);
  }
</style>
</head>
<body>
<main class="letterhead">
  <div class="brand">
    <div class="brand-square"></div>
    <span class="brand-name">Pebble &amp; Fern</span>
  </div>

  <address class="contact">
    <p class="contact-address">47 Willow Lane,<br>ASHGROVE NSW 2190</p>
    <div class="contact-row">
      <svg viewBox="0 0 10 10"><path d="M2 0.5 L4 2.5 L3 3.8 Q4.2 6 6.2 7 L7.5 6 L9.5 8 L8 9.5 Q3.5 9 0.5 2 Z"/></svg>
      <span>(02) 5550 1824</span>
    </div>
    <div class="contact-row">
      <svg viewBox="0 0 10 10"><path d="M2.5 0 H7.5 V10 H2.5 Z M3.5 1 V8 H6.5 V1 Z"/></svg>
      <span>0400 555 219</span>
    </div>
    <div class="contact-row">
      <svg viewBox="0 0 10 10"><path d="M0 2 H10 V8 H0 Z M0.8 2.6 L5 5.6 L9.2 2.6 V3.4 L5 6.4 L0.8 3.4 Z" fill-rule="evenodd"/></svg>
      <span>ashgrove@pebbleandfern.edu.au</span>
    </div>
    <div class="contact-row">
      <svg viewBox="0 0 10 10"><circle cx="5" cy="5" r="4.6"/></svg>
      <span>pebbleandfern.edu.au</span>
    </div>
  </address>

  <div class="recipient">
    <div class="recipient-name">MAREN HOLLOWAY</div>
    <div>Chief Exective Officer</div>
    <div>City/State, Zip Code</div>
  </div>

  <div class="values-wash" role="img" aria-label="Faint values illustration watermark in soft yellow and blue"></div>

  <section class="body">
    <p>Proin gravida nibh vel velit auctor aliquet. Aenean sollicitudin, lorem quis bibendum auctor, nisi elit consequat ipsum, nec sagittis sem nibh id elit. Duis sed odio sit amet nibh vulputate cursus a sit amet mauris. Morbi accumsan ipsum velit. Nam nec tellus a odio tincidunt auctor a ornare odio. Sed non mauris vitae erat consequat auctor eu in elit. Class aptent taciti sociosqu ad litora torquent ugue. Sed non neque elit. Sed ut imperdiet nisi. Proin condimentum fermentum nunc. Etiam pharetra, imperdiet nisi. Proin condimentum fermentum nunc. Etiam pharetra, erat sed fermentum feugiat, velit mauris egestas quam, ut aliquam massa nisl quis neque. Suspendisse in orci enim.</p>
    <p>This is Inkwell's version of Lorem Ipsum. Proin gravida nibh vel velit auctor aliquet. Aenean sollicitudin, lorem quis bibendum auctor, nisi elit consequat ipsum, nec sagittis sem nibh id elit. Duis sed odio sit amet nibh vulputate cursus a sit amet mauris. Mo rbi accumsan ipsum velit. Nam nec tellus a odio tincidunt auctor a ornare odio. Sed non mauris vitae erat consequat auctor eu in elit. Class aptt consequat auctor eu in elit. Class aptent taciti sociosqu ad litora torquent per conubia nostra, per inceptos himenaeos. Mauris in erat justo.</p>
    <p>Nullam ac urna eu felis dapibus condimentum sit amet a augue. Sed non neque elit. Sed ut imperdiet nisi. Proin condimentum fermentum nunc. Etiam pharetra, erat sed fermentum feugiat, velit mauris egestas quam.Nullam ac urna eu felis dapibus condimentum sit amet a aug pharetra, erat sed fermentum feugiat, velit mauris egestas quam.Nullam ac urna eu felis dapibus condimentum sit amet a augue. Sed non neque elit. Sed ut imperdiet nisi. Proin condimentum fermentum nunc.</p>
  </section>

  <div class="signoff">
    <div>Sincerely,</div>
    <div class="signoff-name">Tobias Reed</div>
  </div>
</main>
</body>
</html>
```